Design Project - Finance Website (Only need PSD)

UPDATED PROJECT (Now only PSD needed)
Need a Wordpress design for a company called "Harrowfield Capital Finance". The company provides finance for corporate clients, businesses and property developers. The design should be business like with appealing colours that communicate trust. I have uploaded a banner and logo to be incorporated or feel free to design something better if you think you can.
** I now only need the PSD
** I want something that is actually designed rather than from a template.
Thanks
Updates
The website will be used for lead generation so the contact form with adjustable fields in the Wordpress backend should be fairly prominent on the page.
I have uploaded a banner and logo for the site. None of the designs I have seen so far were good enough so the first decent design using the new banner and logo provided will win the job. I do not want just a template that has been cut and paste from somewhere else, I want decent design. If anyone provides a decent design then I will give an extra bonus of $150.
Reason: I have uploaded a banner and logo for the site. None of the designs I have seen so far were good enough so the first decent design using the new banner and logo provided will win the job. I do not want just a template that has been cut and paste from somewhere else, I want decent design. If anyone provides a decent design then I will give an extra bonus of $150.
Thanks
Target Market(s)
Business owners & property developers
Industry/Entity Type
Finance
Requirements
Must have
- Contact form on home page that can be altered through the back end eg. ability to add or remove fields. Widgetised sidebars.
Nice to have
- Widgetised footer.

```html
<!DOCTYPE html>
<html lang="en">
<head>
<meta charset="utf-8">
<title>Harrowfield Capital Finance</title>
<link href="https://fonts.googleapis.com/css2?family=Roboto+Condensed:wght@400;700&family=Arimo:ital,wght@0,400;0,700;1,700&display=swap" rel="stylesheet">
<style>
:root{
  --nav-top:#1a86d2;
  --nav-bottom:#0a62ad;
  --brand-blue:#0f7ccc;
  --heading-blue:#1479c9;
  --green:#8cc43e;
  --green-dark:#4b8a12;
  --page-bg:#f4f4f4;
  --panel:#ffffff;
  --text:#333333;
  --muted:#777777;
  --line:#d6d6d6;
  --footer:#4a4a4a;
  --footer-base:#3b3b3b;
  --sky-top:#3f8fd8;
  --sky-bottom:#a9d3f2;
}
*{box-sizing:border-box;margin:0;padding:0}
html,body{width:1089px;height:1200px;overflow:hidden;background:var(--page-bg)}
body{font-family:"Arimo",Arial,sans-serif;color:var(--text)}
.page{position:relative;width:1000px;height:1102px;transform:scale(1.089);transform-origin:0 0;background:var(--page-bg)}

/* navigation */
.main-nav{position:absolute;left:0;top:0;width:1000px;height:43px;background:linear-gradient(var(--nav-top),var(--nav-bottom));border-bottom:3px solid #0b5597}
.main-nav ul{list-style:none;display:flex;position:absolute;left:54px;top:7px}
.main-nav li{height:36px;display:flex;align-items:center;padding:0 17px;color:#fff;font-size:14.5px;border-right:1px solid rgba(0,0,0,.25)}
.main-nav li:last-child{border-right:0}
.main-nav li.is-current{background:linear-gradient(#fff,#eaeaea);color:var(--brand-blue);border-radius:4px 4px 0 0;padding:0 12px}

/* header */
.brand{position:absolute;left:56px;top:80px;display:flex;align-items:center;gap:8px;font-family:"Roboto Condensed",sans-serif;font-weight:700;font-size:17px;color:var(--brand-blue);line-height:1.1;width:150px}
.brand-mark{width:14px;height:14px;background:var(--brand-blue);flex:none}
.search{position:absolute;left:684px;top:98px;width:269px;height:31px;border:1px solid var(--line);border-radius:3px;background:#fff;font-size:12px;color:#999;padding:8px 9px}
.search svg{position:absolute;right:7px;top:8px}

/* main panel */
.content-panel{position:absolute;left:52px;top:149px;width:905px;height:788px;background:var(--panel);border-radius:5px 5px 0 0;box-shadow:0 0 3px rgba(0,0,0,.15)}
.hero{position:absolute;left:59px;top:154px;width:892px;height:280px;border-radius:6px 6px 0 0;background:linear-gradient(var(--sky-top),var(--sky-bottom));overflow:hidden}
.hero-city{position:absolute;right:0;top:34px;width:520px;height:246px;background:linear-gradient(#d7dee6,#e9eef2 60%,#cfd9e2)}
.hero-copy{position:absolute;left:18px;top:38px;font-family:"Roboto Condensed",sans-serif;color:#fff;font-size:28px;line-height:36px}
.hero-copy b{font-weight:700}
.hero-copy .wide{margin-top:10px;display:block}
.cta{position:absolute;left:18px;top:174px;width:209px;height:55px;border-radius:7px;background:linear-gradient(#79b82b,var(--green-dark));box-shadow:0 2px 3px rgba(0,0,0,.3);color:#fff;font-weight:700;font-size:20px;display:flex;align-items:center;padding-left:26px;gap:14px}
.cta span.arrow{width:24px;height:24px;border-radius:50%;background:#fff;display:flex;align-items:center;justify-content:center}

/* news strip */
.news-strip{position:absolute;left:72px;top:418px;width:866px;height:112px;background:#fff;border-radius:6px;box-shadow:0 1px 5px rgba(0,0,0,.25)}
.whats-new{position:absolute;left:15px;top:14px}
.whats-new h2{font-family:"Roboto Condensed",sans-serif;color:var(--green);font-size:20px;display:flex;align-items:center;gap:6px}
.whats-new ul{list-style:none;margin-top:8px;font-size:12px;line-height:17px}
.whats-new li b{font-weight:700}
.whats-new a{color:var(--brand-blue);font-weight:700;text-decoration:none}
.case-studies{position:absolute;left:563px;top:9px;width:296px;height:93px;border-left:3px solid var(--green)}
.case-studies h3{height:26px;width:205px;background:var(--green);color:#fff;font-family:"Roboto Condensed",sans-serif;font-size:17px;padding:3px 10px;border-radius:0 12px 0 0}
.case-studies p{font-size:12px;line-height:16px;padding:8px 0 0 10px;width:190px}
.case-studies a{display:block;padding-left:10px;font-size:12px;font-weight:700;font-style:italic;color:var(--brand-blue);text-decoration:none}
.case-art{position:absolute;right:8px;top:10px;width:80px;height:80px;border-radius:4px;background:linear-gradient(#f2f2f2,#dcdcdc)}

/* welcome copy */
.welcome{position:absolute;left:75px;top:547px;width:542px}
.welcome h1{font-family:"Roboto Condensed",sans-serif;color:var(--heading-blue);font-size:21px;font-weight:700;margin-bottom:4px}
.welcome p{font-size:11.8px;line-height:15.6px;text-align:justify;margin-bottom:15.6px;hyphens:auto}

/* contact form */
.contact-widget{position:absolute;left:635px;top:547px;width:301px;height:350px}
.contact-widget::before{content:"";position:absolute;inset:0 0 180px 0;border:1px solid #e2e2e2;border-bottom:0;border-radius:5px 5px 0 0;-webkit-mask-image:linear-gradient(#000 60%,transparent);mask-image:linear-gradient(#000 60%,transparent)}
.contact-widget h2{position:relative;font-family:"Roboto Condensed",sans-serif;color:var(--heading-blue);font-size:20px;padding:5px 17px;height:34px;border-bottom:1px solid #e6e6e6}
.field{position:absolute;left:16px;width:269px;height:31px;border:1px solid var(--line);border-radius:3px;background:#fff;font-size:12px;color:var(--muted);padding:8px 10px}
.field.comments{height:121px}
.submit{position:absolute;left:17px;top:303px;width:73px;height:31px;border:1px solid #4c8a1a;border-radius:2px;background:linear-gradient(#8cc454,#5d9a22);color:#fff;font-weight:700;font-size:13px;display:flex;align-items:center;justify-content:center}

/* footer */
.site-footer{position:absolute;left:0;top:918px;width:1000px;height:134px;background:var(--footer)}
.footer-col{position:absolute;top:30px;color:#fff}
.footer-col h4{font-family:"Roboto Condensed",sans-serif;color:var(--green);font-size:18px;margin-bottom:4px}
.footer-col ul{list-style:none;font-size:12px;line-height:16px}
.footer-col li::before{content:"\25CF";margin:0 4px 0 2px;font-size:10px}
.footer-contact{position:absolute;left:807px;top:38px;color:#fff;font-size:13px;line-height:16px}
.footer-contact h4{font-family:"Roboto Condensed",sans-serif;color:var(--green);font-size:18px;margin-bottom:6px}
.footer-base{position:absolute;left:0;top:1052px;width:1000px;height:50px;background:var(--footer-base);color:#fff;font-size:13px;padding:19px 57px}
</style>
</head>
<body>
<div class="page">
  <nav class="main-nav">
    <ul>
      <li class="is-current">Home</li>
      <li>Services</li>
      <li>Representative Transactions</li>
      <li>About Us</li>
      <li>Media &amp; Information</li>
      <li>Contact Us</li>
    </ul>
  </nav>

  <div class="brand"><span class="brand-mark"></span><span>Harrowfield Capital Finance</span></div>
  <div class="search">search
    <svg width="14" height="14" viewBox="0 0 14 14"><circle cx="8" cy="6" r="4" fill="none" stroke="#999" stroke-width="1.5"/><line x1="5" y1="9" x2="1.5" y2="12.5" stroke="#999" stroke-width="2"/></svg>
  </div>

  <div class="content-panel"></div>

  <section class="hero">
    <div class="hero-city" role="img" aria-label="Photograph of modern office towers against a blue sky"></div>
    <div class="hero-copy">
      <div><b>Compare</b> several capital provider rates</div>
      <div><b>Optimise</b> your capital returns</div>
      <div class="wide">Access to <b>Realestate</b> and hedge funds</div>
    </div>
    <div class="cta">Look &amp; Apply
      <span class="arrow"><svg width="10" height="10" viewBox="0 0 10 10"><path d="M3 1l4 4-4 4" fill="none" stroke="#4b8a12" stroke-width="2"/></svg></span>
    </div>
  </section>

  <section class="news-strip">
    <div class="whats-new">
      <h2><svg width="20" height="20" viewBox="0 0 20 20"><rect x="1" y="2" width="12" height="8" rx="3" fill="none" stroke="#1479c9" stroke-width="2.5"/><rect x="7" y="9" width="12" height="8" rx="3" fill="none" stroke="#1479c9" stroke-width="2.5"/></svg>What’s New</h2>
      <ul>
        <li><b>23 MAY12 |</b> Lorem ipsum dolor sit amet, consectetur adipiscing elit. Aliquamn uere metus. <a>[...]</a></li>
        <li><b>22MAY12 |</b> Nullam vel imperdiet lorem. Aenean quis consequatuas tempor sagittis&nbsp; <a>[...]</a></li>
        <li><b>18 MAY12 |</b> Cras lorem felis, dapibus ac tempus in, semper et lorem. Integer placerat dictu <a>[...]</a></li>
      </ul>
    </div>
    <div class="case-studies">
      <h3>Case studies</h3>
      <p>Aliquam in po lor suere metus. Nulla m vel imp ikd erdiet lorem.</p>
      <a>&#9656; read all</a>
      <div class="case-art" role="img" aria-label="Illustration of a stack of books with a computer mouse"></div>
    </div>
  </section>

  <article class="welcome">
    <h1>Welcome to Harrowfield</h1>
    <p>Lorem ipsum dolor sit amet, consectetur adipiscing elit. Aliquam in posuere metus. Nullam vel imperdiet lorem. Aenean quis consequat mi. Aliquam luctus tempor sagittis. Cras lorem felis, dapibus ac tempus in, semper et lorem. Integer placerat dictum enim, in auctor velit vestibulum pulvinar. Aenean condimen&shy;tum tortor nec arcu pretium ultrices. Phasellus sed sem velit. Aenean risus arcu, consequat vitae lacinia quis, blandit at sem. Integer ut libero turpis, vel porta est. Vivamus consequat, eros non vestibulum viverra, dui nunc ultrices neque, blandit congue ligula tortor eget quam. Mauris mattis malesuada felis, non malesuada mauris accumsan vel. Aliquam ultrices purus ac augue pharetra elementum. Sed tellus lectus, mollis vel tristique ac, vestibulum et dolor.</p>
    <p>Curabitur euismod mi in nibh pulvinar molestie. Praesent non mattis augue. Cras a nulla quis metus aliquet auctor. Nulla eu tellus purus, ac tristique tellus. Class aptent taciti sociosqu ad litora torquent per conubia nostra, per inceptos himenaeos. Pellentesque consectetur ante quis mi sodales quis volutpat sem elementum. Aenean vel mauris ut est faucibus molestie.</p>
    <p>Vestibulum ante ipsum primis in faucibus orci luctus et ultrices posuere cubilia Curae; Maecenas aliquet cursus porta. Donec congue metus id dui scelerisque semper vitae vitae mi. Praesent quis lectus et tortor luctus eleifend eget in sem. Proin gravida dui auctor tellus molestie consectetur. Nunc turpis justo, vulputate ultricies lacinia ac, ultricies in tortor. Morbi vulputate metus vitae massa consequat ullamcor&shy;per vestibulum leo eleifend. Pellentesque laoreet eleifend mauris in iaculis. Proin auctor magna quis lorem lobortis quis vulputate ipsum pulvinar. Etiam eu turpis nec velit tempus sollicitudin. Vivamus inter&shy;dum velit vel magna interdum euismod vestibulum libero volutpat.</p>
  </article>

  <aside class="contact-widget">
    <h2>Contact Us</h2>
    <div class="field" style="top:48px">Name</div>
    <div class="field" style="top:89px">Email</div>
    <div class="field" style="top:131px">Phone</div>
    <div class="field comments" style="top:172px">Comments</div>
    <div class="submit">Submit</div>
  </aside>

  <footer class="site-footer">
    <div class="footer-col" style="left:56px"><h4>Services</h4><ul><li>Tincidunt sitamet</li><li>Vestibulum ante</li><li>Primis in faucibus</li><li>Oorci luctuseto</li></ul></div>
    <div class="footer-col" style="left:215px"><h4>About Us</h4><ul><li>Tincidunt sitamet</li><li>Vestibulum ante</li><li>Primis in faucibus</li><li>Oorci luctuseto</li></ul></div>
    <div class="footer-col" style="left:389px"><h4>Media</h4><ul><li>Tincidunt sitamet</li><li>Vestibulum ante</li><li>Primis in faucibus</li><li>Oorci luctuseto</li></ul></div>
    <div class="footer-contact"><h4>Contact Details</h4>1 (555) 014-2287<br>enquiries@harrowfield.example</div>
  </footer>
  <div class="footer-base">Copyright © 2012 Harrowfield Capital Finance. All rights reserved.</div>
</div>
</body>
</html>
```